Director of a child care centre business card

Corinne Helbrook - Director/ Owner
418 Fernlow Rd
Kellmore, 3287
Phone - 03 9581-4726
Fax - 03 95814727
info@tinybrambles.com.au
www.tinybrambles.com.au

Also needing another card same information but the name will be Yvette Colder - Centre Director

```html
<!DOCTYPE html>
<html lang="en">
<head>
<meta charset="utf-8">
<title>Tiny Brambles – Business Cards</title>
<link href="https://fonts.googleapis.com/css2?family=Josefin+Sans:wght@300;400&family=Oswald:wght@500&display=swap" rel="stylesheet">
<style>
  :root {
    --bg: #ece9e4;
    --navy: #2b5b88;
    --navy-deep: #23507b;
    --pink: #e85aa8;
    --green: #9ccb3b;
    --white: #ffffff;
    --panel: #fbfbfb;
  }
  * { margin: 0; padding: 0; box-sizing: border-box; }
  html, body { width: 1127px; height: 1200px; overflow: hidden; background: var(--bg); }
  .sheet { position: relative; width: 1127px; height: 1200px; }

  .card {
    position: absolute; left: 113px; width: 900px; height: 514px;
    background: linear-gradient(160deg, var(--navy) 0%, var(--navy-deep) 100%);
    border-radius: 4px; overflow: hidden;
    box-shadow: 0 8px 20px rgba(0,0,0,0.18);
  }
  .card--back { top: 52px; }
  .card--front { top: 634px; }

  .brand { position: absolute; text-align: center; font-family: "Josefin Sans", sans-serif; }
  .brand__name { color: var(--pink); font-weight: 400; line-height: 1; }
  .brand__tag { color: var(--white); font-weight: 300; letter-spacing: 1px; }

  .card--back .brand { left: 40px; top: 222px; width: 270px; }
  .card--back .brand__name { font-size: 38px; }
  .card--back .brand__tag { font-size: 15px; margin-top: 6px; }

  .card--front .brand { left: 0; right: 0; top: 210px; }
  .card--front .brand__name { font-size: 72px; }
  .card--front .brand__tag { font-size: 24px; margin-top: 10px; letter-spacing: 2px; }

  .name-tag {
    position: absolute; left: 330px; top: 70px; width: 460px; height: 92px;
    background: var(--panel); border-radius: 28px; padding: 14px 26px;
  }
  .name-tag__name {
    font-family: "Oswald", sans-serif; font-weight: 500; font-size: 38px;
    color: var(--green); line-height: 1.05;
  }
  .name-tag__role {
    font-family: "Josefin Sans", sans-serif; font-weight: 300; font-size: 22px;
    color: var(--pink); letter-spacing: 1px;
  }
  .bow {
    position: absolute; left: 760px; top: 42px; width: 80px; height: 56px;
    border-radius: 28px; background: var(--pink); opacity: 0.85;
  }

  .contact {
    position: absolute; left: 345px; top: 190px; width: 520px; height: 300px;
    background: var(--panel); border-radius: 34px; padding: 22px 28px;
    font-family: "Josefin Sans", sans-serif; font-weight: 300; font-size: 34px;
    line-height: 1.25; color: var(--green); font-style: normal;
  }
</style>
</head>
<body>
<main class="sheet">

  <section class="card card--back" aria-label="Business card, contact side">
    <div class="brand">
      <p class="brand__name">Tiny Brambles</p>
      <p class="brand__tag">Child Care And Kinder</p>
    </div>

    <div class="name-tag">
      <p class="name-tag__name">Corinne Helbrook</p>
      <p class="name-tag__role">Director / Owner</p>
    </div>
    <div class="bow" role="img" aria-label="Pink ribbon bow decoration"></div>

    <address class="contact">
      418 Fernlow Rd<br>
      Kellmore, 3287<br>
      Phone - 03 9581-4726<br>
      Fax - 03 95814727<br>
      info@tinybrambles.com.au<br>
      www.tinybrambles.com.au
    </address>
  </section>

  <section class="card card--front" aria-label="Business card, brand side">
    <div class="brand">
      <p class="brand__name">Tiny Brambles</p>
      <p class="brand__tag">Child Care And Kinder</p>
    </div>
  </section>

</main>
</body>
</html>
```